Anzeigengestaltung für eine Stellenanzeige
Zielgruppe
Stellenanzeige
Wir sind eine Druckerei. Wir suchen für unsere Druckerei einen Buchhalter/in oder bzw. auch für das Rechnungswesen.
Aufgabenstellung
Wir möchten eine Stellenanzeige mit klarer und schneller Wirkung , keine Fließtextanzeige und einer unnötigen Beschreibung wie toll unserer Druckerei ausgestattet ist. Die Anzeige darf bunt und lustig sein Wortspiele wie Zahlenbändiger o.ä. sind erlaubt. Die Stelle soll für 30 bis 40 Stunden Wochenarbeitsstunden ausgeschrieben sein.
Mehr möchten wir gar nicht sagen wir sind ja nicht die kreativsten :-)
Unsere Hausfarbe sind HKS 38 und HKS 6

```html
<!DOCTYPE html>
<html lang="de">
<head>
<meta charset="utf-8">
<title>Stellenanzeige Buchhalter/in</title>
<link href="https://fonts.googleapis.com/css2?family=Inter:wght@300;400;700&display=swap" rel="stylesheet">
<style>
  :root {
    --orange: #dc8a27;
    --navy: #10294a;
    --ink: #1a1a1a;
    --paper: #ffffff;
    --pea: #5fae3a;
  }
  * { margin: 0; padding: 0; box-sizing: border-box; }
  html, body { width: 1200px; height: 848px; overflow: hidden; background: var(--paper); }
  .ad {
    position: relative; width: 1200px; height: 848px; background: var(--paper);
    font-family: "Inter", Arial, sans-serif; color: var(--ink);
  }
  .visual {
    position: absolute; left: 0; top: 0; width: 1143px; height: 660px;
    border-bottom-right-radius: 30px;
    background:
      radial-gradient(ellipse at 95% 35%, #e9c7a8 0%, rgba(233,199,168,0) 22%),
      radial-gradient(ellipse at 50% 50%, #cfe6bd 0%, #a8d489 55%, #8cc46a 100%);
  }
  .frame { position: absolute; left: 0; top: 0; width: 1152px; height: 668px; }
  .message {
    position: absolute; left: 0; top: 160px; width: 843px; height: 314px;
    background: rgba(255,255,255,0.82);
    border: 1.5px solid var(--orange); border-left: none;
    border-radius: 0 20px 20px 0;
  }
  .headline {
    position: absolute; left: 54px; top: 30px;
    color: var(--orange); font-weight: 700; font-size: 56px; line-height: 73px;
    letter-spacing: -0.3px;
  }
  .subline {
    position: absolute; left: 56px; top: 188px;
    font-weight: 300; font-size: 37px; line-height: 46px; letter-spacing: 0.2px;
  }
  .footer { position: absolute; left: 0; top: 690px; width: 1200px; font-size: 18.5px; line-height: 27px; }
  .contact-address { position: absolute; left: 56px; top: 0; }
  .contact-address strong { font-weight: 700; }
  .contact-lines { position: absolute; left: 307px; top: 0; }
  .brand {
    position: absolute; right: 52px; top: 8px;
    display: flex; align-items: center; gap: 14px;
  }
  .brand-square { width: 62px; height: 62px; background: var(--orange); border-radius: 8px; }
  .brand-name { color: var(--navy); font-weight: 700; font-size: 31px; letter-spacing: 0.5px; }
</style>
</head>
<body>
<div class="ad">
  <div class="visual" role="img" aria-label="Foto: grüne Erbsen in exakten Reihen auf weißem Grund, eine Hand setzt eine einzelne Erbse"></div>
  <svg class="frame" viewBox="0 0 1152 668" aria-hidden="true">
    <path d="M1147 0 V630 A30 30 0 0 1 1117 660 H0" fill="none" stroke="var(--orange)" stroke-width="8"/>
  </svg>

  <section class="message">
    <h1 class="headline">Wir lieben Menschen, die<br>es ganz genau nehmen</h1>
    <p class="subline">Denn wir suchen eine/einen Buchhalter/in<br>mit Hang zum Rechnungswesen.</p>
  </section>

  <footer class="footer">
    <address class="contact-address" style="font-style:normal">
      <strong>Kontakt:</strong><br>
      Kessler &amp; Brandt GmbH<br>
      Lindenhofweg 7<br>
      49201 Dissen
    </address>
    <div class="contact-lines">
      Telefon: +49 (0) 5421 3307-0<br>
      Telefax: +49 (0) 5421 3307-19<br>
      info@kesslerbrandt-druck.de
    </div>
    <div class="brand">
      <span class="brand-square"></span>
      <span class="brand-name">KESSLER &amp; BRANDT</span>
    </div>
  </footer>
</div>
</body>
</html>
```